Quarveling stickers design for our main topics (for example: agile and Kanban)

We are looking for sticker design, that will reflect our cooperate identity and can be used for the different topics in our company. We would like to start with our Agile Coaching Offers with a Kanban Sticker saying "stop starting, start finishing", A bad example can be find in the file upload ;)
Check out our homepage to get a feeling for the cooperate identity (www.quarveling.ch)

Target Market(s)

Customers and trainees from our trainings

Industry/Entity Type

Consulting

Colors
0355a3
fbed22

Requirements
Must have
• a cool design thats fits to our customer design
the 2 lines can be changed for future stickers ... like in the example "stop starting, start finishing" and "we show you how"
Nice to have
• -
Should not have
• -

```html
<!DOCTYPE html>
<html lang="en">
<head>
<meta charset="utf-8">
<title>Quarveling Kanban Stickers</title>
<link rel="stylesheet" href="https://fonts.googleapis.com/css2?family=Roboto:ital,wght@0,400;1,300;1,700&display=swap">
<style>
  :root {
    --brand-blue: #0a3de6;
    --brand-navy: #1b3494;
    --ink: #1a1a1a;
    --paper: #ffffff;
    --frame-grey: #dedede;
    --panel-top: #f7f7f7;
    --panel-bottom: #d9d9d9;
    --stage-light: #fafafa;
    --stage-mid: #e2e2e2;
  }
  html, body {
    margin: 0;
    padding: 0;
    width: 1200px;
    height: 1000px;
    overflow: hidden;
  }
  .stage {
    width: 1200px;
    height: 1000px;
    background: linear-gradient(180deg, var(--stage-light) 0%, var(--stage-mid) 50%, var(--stage-light) 100%);
  }
  .stage svg { display: block; }
  .slogan {
    font-family: "Roboto", Arial, sans-serif;
    font-style: italic;
  }
  .slogan--light { font-weight: 300; }
  .slogan--bold { font-weight: 700; }
  .brand-name {
    font-family: "Roboto", Arial, sans-serif;
    font-weight: 400;
    fill: var(--ink);
  }
  .web-address {
    font-family: "Roboto", Arial, sans-serif;
    font-weight: 400;
    fill: var(--paper);
  }
</style>
</head>
<body>
<main class="stage">
  <svg width="1200" height="1000" viewBox="0 0 1200 1000" xmlns="http://www.w3.org/2000/svg">
    <defs>
      <linearGradient id="panelFill" x1="0" y1="0" x2="0" y2="1">
        <stop offset="0" stop-color="var(--panel-top)"/>
        <stop offset="1" stop-color="var(--panel-bottom)"/>
      </linearGradient>
      <linearGradient id="blueFill" x1="0" y1="0" x2="0" y2="1">
        <stop offset="0" stop-color="var(--brand-blue)"/>
        <stop offset="1" stop-color="var(--brand-navy)"/>
      </linearGradient>
    </defs>

    <!-- Sticker one: wide banner with address tab -->
    <g class="sticker sticker--banner">
      <polygon class="banner-accent" points="193,267 415,267 318,459 90,459" fill="url(#blueFill)"/>
      <polygon class="banner-frame" points="210,280 1097,280 1012,444 118,444" fill="var(--frame-grey)"/>
      <polygon class="banner-face" points="222,290 1080,290 1002,436 134,436" fill="url(#panelFill)"/>
      <polygon class="address-tab" points="960,337 1040,337 972,462 425,462 455,402 922,402" fill="url(#blueFill)"/>

      <text class="slogan" x="208" y="363" font-size="38" fill="var(--brand-navy)">
        <tspan class="slogan--light">Stop starting, </tspan><tspan class="slogan--bold">Start finishing</tspan>
      </text>

      <rect class="brand-square" x="808" y="312" width="46" height="46" fill="var(--brand-blue)"/>
      <text class="brand-name" x="862" y="325" font-size="30">Quarveling ag</text>

      <text class="web-address" x="694" y="441" font-size="24" text-anchor="middle">www.quarveling.ch/kanban-coaching</text>
    </g>

    <!-- Sticker two: split panel with headline lines -->
    <g class="sticker sticker--split">
      <polygon class="split-body" points="380,528 1075,528 988,692 300,692" fill="url(#blueFill)"/>

      <polygon class="brand-panel-frame" points="178,516 395,516 295,707 70,707" fill="var(--frame-grey)"/>
      <polygon class="brand-panel-face" points="186,524 380,524 288,699 84,699" fill="url(#panelFill)"/>

      <polygon class="finish-tab-frame" points="528,640 890,640 930,563 1026,563 950,711 500,711" fill="var(--frame-grey)"/>
      <polygon class="finish-tab-face" points="536,648 896,648 937,572 1012,572 944,703 514,703" fill="url(#panelFill)"/>

      <rect class="brand-square" x="152" y="594" width="40" height="40" fill="var(--brand-blue)"/>
      <text class="brand-name" x="198" y="600" font-size="24">Quarveling ag</text>

      <text class="slogan slogan--light" x="420" y="609" font-size="44" fill="var(--paper)">Stop starting,</text>
      <line class="headline-rule" x1="712" y1="601" x2="881" y2="601" stroke="var(--paper)" stroke-width="3"/>
      <line class="headline-rule" x1="340" y1="661" x2="510" y2="661" stroke="var(--paper)" stroke-width="3"/>
      <text class="slogan slogan--bold" x="565" y="688" font-size="44" fill="var(--brand-navy)">Start finishing</text>
    </g>
  </svg>
</main>
</body>
</html>
```